Tarvel Ridge LLC

Need Professional Business cards for New Investment Fund

Target Market(s)

High Quality investors

Industry/Entity Type

Financial

Contact Information for Business Card

Phone Number +1 555 284 6193
Name Pavel Orlinsky
Title Fund Manager
email po@FundTarvel.example
Website www.FundTarvel.example

Colors

Designer to choose colors to be used in the design.

Requirements
Must have
• Must have our Logo and all of the above. Must be made so lettering and loge can be raised

```html
<!DOCTYPE html>
<html lang="en">
<head>
<meta charset="utf-8">
<title>Tarvel Ridge LLC – Business Card</title>
<link rel="stylesheet" href="https://fonts.googleapis.com/css2?family=Saira+Condensed:wght@500;600&family=Arimo:wght@400&display=swap">
<style>
  :root {
    --backdrop: #2b2b2b;
    --card: #1f1f1f;
    --silver: #a9a9a9;
    --ink-dim: #5a5a5a;
    --white: #f4f4f4;
    --green: #5cc04a;
  }
  * { margin: 0; padding: 0; box-sizing: border-box; }
  html, body { width: 1200px; height: 900px; overflow: hidden; }
  body {
    background: var(--backdrop);
    display: flex;
    flex-direction: column;
    align-items: center;
    justify-content: center;
    gap: 40px;
  }
  .card {
    position: relative;
    width: 640px;
    height: 366px;
    background: var(--card);
    overflow: hidden;
  }
  /* Front */
  .card-front {
    display: flex;
    flex-direction: column;
    align-items: center;
    justify-content: center;
  }
  .brand-mark {
    width: 40px;
    height: 40px;
    background: var(--silver);
    margin-bottom: 22px;
  }
  .brand-name {
    font-family: "Saira Condensed", sans-serif;
    font-weight: 600;
    font-size: 56px;
    letter-spacing: 6px;
    color: var(--silver);
    line-height: 1;
  }
  .brand-url {
    margin-top: 40px;
    font-family: "Saira Condensed", sans-serif;
    font-weight: 500;
    font-size: 15px;
    letter-spacing: 5px;
    color: var(--ink-dim);
    text-transform: uppercase;
  }
  /* Back */
  .card-back {
    display: flex;
    align-items: center;
    padding: 0 0 20px 0;
  }
  .identity {
    width: 300px;
    text-align: right;
    padding-right: 22px;
    margin-left: 30px;
  }
  .person-name {
    font-family: "Saira Condensed", sans-serif;
    font-weight: 600;
    font-size: 40px;
    letter-spacing: 1px;
    color: var(--white);
    line-height: 1;
    text-transform: uppercase;
  }
  .person-title {
    margin-top: 4px;
    font-family: "Arimo", sans-serif;
    font-size: 13px;
    letter-spacing: 1.5px;
    color: var(--green);
  }
  .divider {
    width: 2px;
    height: 96px;
    background: var(--green);
  }
  .contacts {
    list-style: none;
    margin-left: 44px;
    display: flex;
    flex-direction: column;
    gap: 9px;
  }
  .contact-item {
    display: flex;
    align-items: center;
    gap: 14px;
    font-family: "Arimo", sans-serif;
    font-size: 14px;
    letter-spacing: 1px;
    color: var(--white);
  }
  .contact-icon { width: 14px; height: 14px; flex: none; }
  .accent-band {
    position: absolute;
    left: 0; right: 0; bottom: 0;
    height: 10px;
    background: var(--green);
  }
</style>
</head>
<body>
  <section class="card card-front">
    <div class="brand-mark"></div>
    <h1 class="brand-name">TARVEL RIDGE</h1>
    <p class="brand-url">www.FundTarvel.example</p>
  </section>

  <section class="card card-back">
    <div class="identity">
      <h2 class="person-name">Pavel Orlinsky</h2>
      <p class="person-title">Fund Manager</p>
    </div>
    <div class="divider"></div>
    <ul class="contacts">
      <li class="contact-item">
        <svg class="contact-icon" viewBox="0 0 14 14" aria-hidden="true"><rect x="3" y="0.8" width="8" height="12.4" rx="1.2" fill="none" stroke="#5cc04a" stroke-width="1.2"/><line x1="5.5" y1="11" x2="8.5" y2="11" stroke="#5cc04a" stroke-width="1"/></svg>
        +15552846193
      </li>
      <li class="contact-item">
        <svg class="contact-icon" viewBox="0 0 14 14" aria-hidden="true"><rect x="0.8" y="2.6" width="12.4" height="8.8" fill="none" stroke="#5cc04a" stroke-width="1.2"/><polyline points="0.8,2.6 7,7.6 13.2,2.6" fill="none" stroke="#5cc04a" stroke-width="1.2"/></svg>
        www.FundTarvel.example
      </li>
      <li class="contact-item">
        <svg class="contact-icon" viewBox="0 0 14 14" aria-hidden="true"><circle cx="7" cy="7" r="6" fill="none" stroke="#5cc04a" stroke-width="1.2"/><ellipse cx="7" cy="7" rx="2.6" ry="6" fill="none" stroke="#5cc04a" stroke-width="1"/><line x1="1" y1="7" x2="13" y2="7" stroke="#5cc04a" stroke-width="1"/></svg>
        po@FundTarvel.example
      </li>
    </ul>
    <div class="accent-band"></div>
  </section>
</body>
</html>
```